Maple Ledger Business Card

Colors can be blue, grey and white as you see in the attached logo. Needs to have a spot for name, title, phone, email, address, and website. There also needs to be a spot for an agent's picture.

Contact Information for Business Card

See project description.

Colors

Designer to choose colors to be used in the design.

```html
<!DOCTYPE html>
<html lang="en">
<head>
<meta charset="utf-8">
<title>Maple Ledger Business Card</title>
<link href="https://fonts.googleapis.com/css2?family=Lato:wght@400;700&display=swap" rel="stylesheet">
<style>
  :root {
    --page-bg: #d4d6d9;
    --card-dark: #555658;
    --card-light: #ffffff;
    --brand-blue: #2b74c1;
    --text-grey: #3d3e40;
    --white: #ffffff;
  }
  * { box-sizing: border-box; margin: 0; padding: 0; }
  html, body {
    width: 1200px; height: 800px; overflow: hidden;
    background: var(--page-bg);
    font-family: "Lato", sans-serif;
  }
  .canvas { position: relative; width: 1200px; height: 800px; }

  .card {
    position: absolute; width: 600px; height: 343px;
    box-shadow: 0 6px 18px rgba(0,0,0,0.18);
  }

  /* Back of card */
  .card-back { left: 540px; top: 50px; background: var(--card-dark); color: var(--white); }
  .card-back .brand {
    position: absolute; left: 0; right: 0; top: 120px;
    text-align: center;
  }
  .brand-name {
    display: inline-flex; align-items: center; gap: 12px;
    font-weight: 700; font-size: 34px; letter-spacing: 2px;
  }
  .brand-mark { width: 18px; height: 18px; background: currentColor; display: inline-block; }
  .card-back .web {
    position: absolute; left: 0; right: 0; top: 250px;
    text-align: center; font-size: 15px; letter-spacing: 2.5px;
  }

  /* Front of card */
  .card-front { left: 60px; top: 420px; background: var(--card-light); color: var(--text-grey); }
  .photo-frame {
    position: absolute; left: 110px; top: 34px; width: 190px; height: 210px;
    border: 3px solid var(--brand-blue); padding: 6px; background: var(--card-light);
  }
  .photo {
    width: 100%; height: 100%;
    background: linear-gradient(160deg, #5a4a3e 0%, #2c3140 55%, #1e2433 100%);
  }
  .accent-bar {
    position: absolute; left: 34px; top: 245px; width: 14px; height: 46px;
    background: var(--brand-blue);
  }
  .agent { position: absolute; left: 78px; top: 248px; }
  .agent-name { color: var(--brand-blue); font-weight: 700; font-size: 25px; letter-spacing: 0.5px; }
  .agent-title { font-size: 18px; letter-spacing: 0.5px; margin-top: 2px; }

  .card-front .brand {
    position: absolute; left: 330px; width: 250px; top: 110px;
    text-align: center; color: var(--brand-blue);
  }
  .card-front .brand-name { font-size: 26px; gap: 10px; }
  .card-front .brand-mark { width: 14px; height: 14px; }

  .contact { position: absolute; left: 335px; top: 185px; font-size: 16px; line-height: 1.3; }
  .address { margin-bottom: 8px; padding-left: 22px; }
  .contact-row { display: flex; align-items: center; gap: 8px; }
  .contact-row svg { width: 14px; height: 14px; flex: none; }
</style>
</head>
<body>
<main class="canvas">

  <section class="card card-back" aria-label="Card back">
    <div class="brand"><span class="brand-name"><span class="brand-mark"></span>MAPLE LEDGER</span></div>
    <p class="web">www.mapleledgerre.com</p>
  </section>

  <section class="card card-front" aria-label="Card front">
    <div class="photo-frame">
      <div class="photo" role="img" aria-label="Agent headshot portrait"></div>
    </div>
    <div class="accent-bar"></div>
    <div class="agent">
      <p class="agent-name">DAN WALSH</p>
      <p class="agent-title">CO-OWNER</p>
    </div>

    <div class="brand"><span class="brand-name"><span class="brand-mark"></span>MAPLE LEDGER</span></div>

    <div class="contact">
      <p class="address">2915 N Harlow Ave, Suite B<br>Carmel Falls, IN 46120</p>
      <p class="contact-row">
        <svg viewBox="0 0 16 16" aria-hidden="true"><path fill="#2b74c1" d="M3.6 1l2.3 3-1.3 1.8c.9 2 2.5 3.6 4.6 4.6L11 9.1l3 2.3-1.4 2.9C7 14 2 9 1.7 3.4z"/></svg>
        (317) 555-0148
      </p>
      <p class="contact-row">
        <svg viewBox="0 0 16 16" aria-hidden="true"><rect x="1" y="3" width="14" height="10" fill="none" stroke="#2b74c1" stroke-width="1.5"/><path d="M1 3l7 6 7-6" fill="none" stroke="#2b74c1" stroke-width="1.5"/></svg>
        danwalsh@mapleledgerre.com
      </p>
      <p class="contact-row">
        <svg viewBox="0 0 16 16" aria-hidden="true"><g fill="none" stroke="#2b74c1" stroke-width="1.3"><circle cx="8" cy="8" r="6.5"/><ellipse cx="8" cy="8" rx="3" ry="6.5"/><path d="M1.5 8h13"/></g></svg>
        www.mapleledgerre.com
      </p>
    </div>
  </section>

</main>
</body>
</html>
```